Career development coaching - school lever to adults, needs a business card

Tandem Lark - An independent Career Advice business that provides 1-2-1 advice,for career development, entrepreneurial support and workshops needs a business card. Our clients of all ages (school leaver to adults looking for a career move) and universities and colleges. We would like the card to be double-sided with a modern, professional look. Looking for something professional yet very creative and original. Want a standard size business card that inspires a second look because it stands out from the rest.

One side of the card to have a design incorporating the logo with Tandem Lark name with the strap line “Helping you find your future” and space for the company website

Other side of the card to the logo/Tandem Lark name and the usual contact information:
Individual Name
Job Title (for example, Director)
Phone number
Email address
Company website address

Facebook, LinkedIn and Twitter links will need to go somewhere (back or front!)

The design will be used for 3 individuals so should be editable so that we can update as needed/as we grow.

Attached is the company logo/colours to be incorporated.

Target Market(s)

1-2-1 advice,for career development, entrepreneurial support and workshops needs a business card. Our clients of all ages (school leaver to adults looking for a career move) and universities and colleges.

Industry/Entity Type

Consulting

Contact Information for Business Card

Individual Name
Phone number
Email address
Company website address

Font styles to use
Sans Serif

Colors
0255a3
3176b5
faa54b
f78f20
85acd3
cfdeed

Requirements
Must have
• use the Tandem Lark Logo in some way - using the colours and the blue/orange palette
• For the logo - hope this makes sense to someone or if they direclty relate to the logo image attached!
• For the Orange:- Pantone 1585 C
• In CMYK : C3 M71 Y100 K0
• For the Blue:- 100% Pantone 7469 C
• In CMYK : C100 M62 Y27 K7
• Please feel free to contact me with any questions for more info
Nice to have
• happy to see any creative designs
Should not have
• Nothing too traditional,

```html
<!DOCTYPE html>
<html lang="en">
<head>
<meta charset="utf-8">
<title>Tandem Lark – Business Card</title>
<link rel="stylesheet" href="https://fonts.googleapis.com/css2?family=Roboto:wght@400;500;700&display=swap">
<style>
  :root {
    --brand-blue: #12628c;
    --brand-orange: #f07430;
    --card-white: #ffffff;
    --text-grey: #666666;
    --faint-grey: #f3f2f3;
    --stage: #3b312c;
  }
  * { box-sizing: border-box; margin: 0; padding: 0; }
  html, body {
    width: 1200px; height: 1000px; overflow: hidden;
    background: var(--stage);
    font-family: "Roboto", Arial, sans-serif;
  }
  .canvas { position: relative; width: 1200px; height: 1000px; }

  .card {
    position: absolute; left: 287px; width: 627px; height: 358px;
    overflow: hidden;
  }

  /* Front */
  .card--front { top: 140px; background: var(--brand-blue); color: var(--card-white); text-align: center; }
  .front__mark {
    position: absolute; left: 50%; top: 210px; width: 70px; height: 70px;
    margin-left: -35px; margin-top: -140px;
    border-radius: 50%; background: var(--brand-orange);
  }
  .front__name {
    position: absolute; left: 0; right: 0; top: 200px;
    font-size: 31px; font-weight: 500; letter-spacing: 2px; text-transform: uppercase;
  }
  .front__tagline {
    position: absolute; left: 0; right: 0; top: 242px;
    font-size: 15px; letter-spacing: 2.2px;
  }
  .front__website {
    position: absolute; left: 0; right: 0; top: 311px;
    font-size: 15px; letter-spacing: 0.2px;
  }

  /* Back */
  .card--back { top: 531px; background: var(--card-white); }
  .back__brand {
    position: absolute; right: 36px; top: 46px;
    font-size: 29px; font-weight: 500; letter-spacing: 2px; text-transform: uppercase;
    color: var(--brand-blue);
  }
  .back__decor {
    position: absolute; left: 410px; top: 154px; width: 200px; height: 200px;
    border-radius: 50%; background: var(--faint-grey);
  }
  .back__accent {
    position: absolute; left: 0; top: 168px; width: 6px; height: 32px;
    background: var(--brand-orange);
  }
  .person { position: absolute; left: 35px; top: 163px; }
  .person__name { font-size: 19px; font-weight: 700; color: var(--brand-blue); letter-spacing: 0.3px; }
  .person__role { font-size: 14px; color: var(--text-grey); margin-top: 1px; }

  .contact-list { position: absolute; left: 35px; top: 233px; list-style: none; }
  .contact-list li {
    display: flex; align-items: center; gap: 4px;
    height: 20px; font-size: 14.5px; color: var(--text-grey);
  }
  .contact-list svg { width: 11px; height: 11px; fill: var(--brand-orange); flex: none; }

  .social-row { position: absolute; left: 35px; top: 304px; display: flex; gap: 7px; }
  .social-row span {
    width: 14px; height: 14px; border: 1.2px solid var(--text-grey); border-radius: 2px;
  }
</style>
</head>
<body>
<main class="canvas">

  <section class="card card--front" aria-label="Card front">
    <div class="front__mark"></div>
    <h1 class="front__name">Tandem Lark</h1>
    <p class="front__tagline">Helping you find your future!</p>
    <p class="front__website">Visit us: www.TandemLark.com</p>
  </section>

  <section class="card card--back" aria-label="Card back">
    <div class="back__decor"></div>
    <h2 class="back__brand">Tandem Lark</h2>
    <div class="back__accent"></div>
    <div class="person">
      <p class="person__name">MAYA HOLT</p>
      <p class="person__role">Director</p>
    </div>
    <ul class="contact-list">
      <li>
        <svg viewBox="0 0 12 12"><path d="M2.5 1 L4.5 1 L5.2 3.6 L3.9 4.6 C4.5 6 5.8 7.4 7.3 8 L8.3 6.8 L11 7.5 L11 9.5 C11 10.3 10.3 11 9.5 11 C5 11 1 7 1 2.5 C1 1.7 1.7 1 2.5 1 Z"/></svg>
        555-0142-7788
      </li>
      <li>
        <svg viewBox="0 0 12 12"><path d="M1 2.5 H11 V9.5 H1 Z M1.6 3 L6 6.4 L10.4 3 Z" fill-rule="evenodd"/></svg>
        info@tandemlark.com
      </li>
      <li>
        <svg viewBox="0 0 12 12"><circle cx="6" cy="6" r="4.8" fill="none" stroke="#f07430" stroke-width="1.1"/><path d="M1.2 6 H10.8 M6 1.2 V10.8" stroke="#f07430" stroke-width="0.9"/><ellipse cx="6" cy="6" rx="2" ry="4.8" fill="none" stroke="#f07430" stroke-width="0.9"/></svg>
        www.tandemlark.com
      </li>
    </ul>
    <div class="social-row" aria-label="Social links">
      <span></span><span></span><span></span>
    </div>
  </section>

</main>
</body>
</html>
```